Copper Hollow Sparkling

Hi all,

Thanks for taking the time to check out our brief.

Copper Hollow is an Australian wine company based in Victoria, and have been around for more than 20 years. We have a well-known sparkling Chardonnay Pinot Noir that needs a package revamp and we need your help!

Check out our current package here: http://www.copperhollowvino.com.au/our-wines/dsp-default_b.cfm?loadref=17

So here's the brief:

1. Use of the Copper Hollow logo (silhouette) and text mandatory - but can be as small/large as required.

2. Design must be shown on a sparkling bottle.

3. Can be closed with cork or crown seal - neck label/hood not mandatory.

4. Front label size to be no larger than 75mm high x 100mm wide. Back label to be no larger than 75mm x 100mm

5. Label does not have to be square/rectangular. Happy to see thoughts outside the box.

6. Design cannot be printed onto the bottle - must be on a label that can be applied to the bottle.

7. Be forward thinking. Be interesting. This design does not have to tie into our still (red and white) wine range.

8. Mandatory information to be shown on front label - a. Wine of Australia - b. Sparkling Chardonnay Pinot Noir

9. Mandatory info for front label - a. 750mL - b. Alcohol e.g. 13.5% ALC/VOL - c. Wine of Australi - d. Producer address (please insert dummy address at this stage - e. standard drinks e.g. approx 8.0 standard drinks (this can also be shown in the standard drinks glass logo) - f. space for a tasting blurb

10. Try to stay away from anything floral or overly girly.

Industry/Entity Type

Floral

Requirements
Must have
• Design must be shown on a sparkling wine bottle & include the full label design separately
Should not have
• Try to stay away from anything too floral and overly girly.

```html
<!DOCTYPE html>
<html lang="en">
<head>
<meta charset="utf-8">
<title>Copper Hollow – Sparkling Chardonnay Pinot Noir – Label Variations</title>
<link rel="stylesheet" href="https://fonts.googleapis.com/css2?family=Sorts+Mill+Goudy&family=Open+Sans:wght@400&display=swap">
<style>
  :root {
    --paper: #ffffff;
    --ink: #1a1a1a;
    --gold: #ecd595;
    --gold-rule: #b89a56;
    --label-light: #2e2e2e;
    --label-dark: #060606;
    --glass-top: #c9a64a;
    --glass-mid: #b9a548;
    --glass-low: #6f6a2a;
  }
  * { box-sizing: border-box; margin: 0; padding: 0; }
  html, body { width: 1200px; height: 1000px; overflow: hidden; background: var(--paper); }
  .sheet { position: relative; width: 1200px; height: 1000px; font-family: "Open Sans", Arial, sans-serif; color: var(--ink); }

  .sheet-title { position: absolute; top: 8px; left: 0; width: 100%; text-align: center; font-size: 11px; line-height: 14px; }

  .size-note { position: absolute; font-size: 7.5px; line-height: 10px; }
  .variation-caption { position: absolute; top: 458px; font-size: 11px; line-height: 14px; }

  /* Label */
  .label { position: absolute; width: 296px; height: 296px; font-family: "Sorts Mill Goudy", Georgia, serif; color: var(--gold); }
  .label-surface { position: absolute; inset: 0; background: radial-gradient(ellipse at 40% 35%, var(--label-light) 0%, #151515 55%, var(--label-dark) 100%); }
  .label--round .label-surface { border-radius: 50%; }
  .label--round .label-surface::before { content: ""; position: absolute; inset: 8px; border: 1px solid var(--gold-rule); border-radius: 50%; }
  .label--rect .label-surface::before { content: ""; position: absolute; inset: 5px; border: 1px solid var(--gold-rule); }
  .label--rect .label-surface::after { content: ""; position: absolute; inset: 9px; border: 1px solid var(--gold-rule); }
  .label--wavy .label-surface { background: none; }
  .label--wavy svg { position: absolute; inset: 0; width: 298px; height: 296px; }

  .brand-dot { position: absolute; left: 132px; top: 24px; width: 32px; height: 32px; border-radius: 50%; background: var(--gold); }
  .brand-name { position: absolute; left: 0; width: 100%; top: 78px; text-align: center; font-size: 12px; line-height: 16px; letter-spacing: 2.6px; }
  .rule { position: absolute; left: 40px; width: 216px; height: 1px; background: var(--gold-rule); }
  .rule--top { top: 104px; }
  .rule--bottom { top: 238px; }
  .wine-name { position: absolute; left: 0; width: 100%; top: 110px; text-align: center; font-size: 33px; line-height: 39px; }
  .origin { position: absolute; left: 0; width: 100%; top: 253px; text-align: center; font-size: 10.5px; line-height: 14px; }

  .bottles { position: absolute; left: 0; top: 0; width: 1200px; height: 1000px; }
  .on-bottle { transform-origin: 0 0; }
</style>
</head>
<body>
<main class="sheet">
  <p class="sheet-title">Copper Hollow_ Chardonnay Pinot Noir 03</p>

  <!-- Flat label artwork -->
  <div class="label label--round" style="left:110px; top:96px;">
    <div class="label-surface" role="img" aria-label="Dark soft-focus bokeh background"></div>
    <span class="brand-dot"></span>
    <p class="brand-name">COPPER HOLLOW</p>
    <span class="rule rule--top"></span>
    <p class="wine-name">Sparkling<br>Chardonnay<br>Pinot Noir</p>
    <span class="rule rule--bottom"></span>
    <p class="origin">Wine of Australia</p>
  </div>
  <span class="size-note" style="left:398px; top:236px;">75 mm</span>

  <div class="label label--rect" style="left:478px; top:91px;">
    <div class="label-surface" role="img" aria-label="Dark soft-focus bokeh background"></div>
    <span class="brand-dot"></span>
    <p class="brand-name">COPPER HOLLOW</p>
    <span class="rule rule--top"></span>
    <p class="wine-name">Sparkling<br>Chardonnay<br>Pinot Noir</p>
    <span class="rule rule--bottom"></span>
    <p class="origin">Wine of Australia</p>
  </div>
  <span class="size-note" style="left:783px; top:238px;">75 mm</span>

  <div class="label label--wavy" style="left:868px; top:93px;">
    <svg viewBox="0 0 298 296" role="img" aria-label="Wavy die-cut label with dark soft-focus bokeh background">
      <defs>
        <radialGradient id="bokeh-wavy" cx="40%" cy="35%" r="75%">
          <stop offset="0" stop-color="#2e2e2e"/>
          <stop offset="0.55" stop-color="#151515"/>
          <stop offset="1" stop-color="#060606"/>
        </radialGradient>
      </defs>
      <path fill="url(#bokeh-wavy)" d="M4,0 L294,0 Q302,29.6 294,59.2 T294,118.4 T294,177.6 T294,236.8 T294,296 L4,296 Q-4,266.4 4,236.8 T4,177.6 T4,118.4 T4,59.2 T4,0 Z"/>
    </svg>
    <span class="brand-dot"></span>
    <p class="brand-name">COPPER HOLLOW</p>
    <span class="rule rule--top"></span>
    <p class="wine-name">Sparkling<br>Chardonnay<br>Pinot Noir</p>
    <span class="rule rule--bottom"></span>
    <p class="origin">Wine of Australia</p>
  </div>
  <span class="size-note" style="left:1175px; top:234px;">75 mm</span>

  <p class="variation-caption" style="left:165px;">Variation - round die-cut</p>
  <p class="variation-caption" style="left:553px;">Variation - rectangular die-cut</p>
  <p class="variation-caption" style="left:955px;">Variation - wavy die-cut</p>

  <!-- Bottles -->
  <svg class="bottles" viewBox="0 0 1200 1000" role="img" aria-label="Sparkling wine bottles in green-gold glass with gold foil capsules">
    <defs>
      <linearGradient id="glass" x1="0" y1="0" x2="0" y2="1">
        <stop offset="0" stop-color="var(--glass-top)"/>
        <stop offset="0.4" stop-color="var(--glass-mid)"/>
        <stop offset="1" stop-color="var(--glass-low)"/>
      </linearGradient>
      <path id="bottle-shape" d="M-30,0 C-36,5 -36,20 -32,40 L-32,170 C-34,250 -88,290 -90,360 L-90,612 Q-90,622 -80,622 L80,622 Q90,622 90,612 L90,360 C88,290 34,250 32,170 L32,40 C36,20 36,5 30,0 Z"/>
    </defs>
    <use href="#bottle-shape" fill="url(#glass)" transform="translate(98,368)"/>
    <use href="#bottle-shape" fill="url(#glass)" transform="translate(445,368)"/>
    <use href="#bottle-shape" fill="url(#glass)" transform="translate(822,368)"/>
  </svg>

  <!-- Labels applied on bottles -->
  <div class="label label--round on-bottle" style="left:28px; top:773px; transform:scale(0.473);">
    <div class="label-surface" role="img" aria-label="Dark soft-focus bokeh background"></div>
    <span class="brand-dot"></span>
    <p class="brand-name">COPPER HOLLOW</p>
    <span class="rule rule--top"></span>
    <p class="wine-name">Sparkling<br>Chardonnay<br>Pinot Noir</p>
    <span class="rule rule--bottom"></span>
    <p class="origin">Wine of Australia</p>
  </div>

  <div class="label label--rect on-bottle" style="left:367px; top:759px; transform:scale(0.53, 0.51);">
    <div class="label-surface" role="img" aria-label="Dark soft-focus bokeh background"></div>
    <span class="brand-dot"></span>
    <p class="brand-name">COPPER HOLLOW</p>
    <span class="rule rule--top"></span>
    <p class="wine-name">Sparkling<br>Chardonnay<br>Pinot Noir</p>
    <span class="rule rule--bottom"></span>
    <p class="origin">Wine of Australia</p>
  </div>

  <div class="label label--wavy on-bottle" style="left:756px; top:773px; transform:scale(0.445, 0.47);">
    <svg viewBox="0 0 298 296" role="img" aria-label="Wavy die-cut label with dark soft-focus bokeh background">
      <path fill="url(#bokeh-wavy)" d="M4,0 L294,0 Q302,29.6 294,59.2 T294,118.4 T294,177.6 T294,236.8 T294,296 L4,296 Q-4,266.4 4,236.8 T4,177.6 T4,118.4 T4,59.2 T4,0 Z"/>
    </svg>
    <span class="brand-dot"></span>
    <p class="brand-name">COPPER HOLLOW</p>
    <span class="rule rule--top"></span>
    <p class="wine-name">Sparkling<br>Chardonnay<br>Pinot Noir</p>
    <span class="rule rule--bottom"></span>
    <p class="origin">Wine of Australia</p>
  </div>
</main>
</body>
</html>
```